Solar WiFi Charging Bench

Sales Brochure using only the colors of the Marigold Color Palette provided.
Municipal Government target customer.
Key Features are as follows:
LED Advertising display
Connection to internet (User Defined)
800W Solar
USB-A and USB-C cell phone charging ports
400ah battery backup with low voltage shutoff
Insulated for -40 Deg C
Wireless cell phone charging
Vandalism resistant.
Theft resistant

```html
<!DOCTYPE html>
<html lang="en">
<head>
<meta charset="utf-8">
<title>Solar WiFi Charging Bench – Marigold Renewables</title>
<link rel="stylesheet" href="https://fonts.googleapis.com/css2?family=Poppins:wght@400;500;600&display=swap">
<style>
  :root {
    --brand-blue: #3d4fa6;
    --brand-green: #7bc143;
    --brand-cyan: #3fb8e0;
    --ink: #1b1b1b;
    --paper: #ffffff;
  }
  html, body {
    margin: 0;
    padding: 0;
    overflow: hidden;
    background: var(--paper);
  }
  .brochure {
    position: relative;
    width: 848px;
    height: 1200px;
    overflow: hidden;
    background: var(--paper);
    font-family: "Poppins", sans-serif;
  }
  .brochure-art {
    position: absolute;
    inset: 0;
    width: 848px;
    height: 1200px;
  }
  .brand-name {
    position: absolute;
    left: 590px;
    top: 40px;
    width: 220px;
    text-align: center;
    color: var(--brand-blue);
    font-weight: 600;
    font-size: 31px;
    line-height: 1.1;
    letter-spacing: 0.5px;
    text-transform: uppercase;
  }
  .brand-mark {
    display: block;
    width: 76px;
    height: 76px;
    margin: 0 auto 36px;
    border-radius: 50%;
    background: var(--brand-cyan);
  }
  .brand-name .brand-sub {
    display: block;
    margin-top: 4px;
    font-size: 15px;
    letter-spacing: 2.5px;
  }
  .feature-list {
    position: absolute;
    left: 40px;
    top: 721px;
    margin: 0;
    padding: 0;
    list-style: none;
    color: var(--ink);
    font-weight: 500;
    font-size: 26.3px;
    line-height: 36.3px;
  }
  .social {
    position: absolute;
    left: 0;
    right: 0;
    top: 1124px;
    text-align: center;
    color: var(--paper);
    font-size: 13px;
    font-weight: 400;
  }
  .social-icons {
    display: flex;
    justify-content: center;
    gap: 13px;
    margin-bottom: 7px;
  }
  .social-dot {
    width: 28px;
    height: 28px;
    border-radius: 50%;
    background: var(--paper);
  }
</style>
</head>
<body>
<main class="brochure">
  <svg class="brochure-art" viewBox="0 0 848 1200" xmlns="http://www.w3.org/2000/svg">
    <defs>
      <linearGradient id="hero-tones" x1="0" y1="0" x2="0" y2="1">
        <stop offset="0" stop-color="#e2e5e7"/>
        <stop offset="0.38" stop-color="#d9dcdd"/>
        <stop offset="0.52" stop-color="#b7b9ad"/>
        <stop offset="0.66" stop-color="#9a8d62"/>
        <stop offset="1" stop-color="#6a573b"/>
      </linearGradient>
      <linearGradient id="faded-tones" x1="0" y1="0" x2="0" y2="1">
        <stop offset="0" stop-color="#f3f5f6"/>
        <stop offset="1" stop-color="#e9ebe9"/>
      </linearGradient>
      <linearGradient id="footer-wave" x1="0" y1="0" x2="1" y2="0">
        <stop offset="0" stop-color="var(--brand-blue)"/>
        <stop offset="1" stop-color="var(--brand-cyan)"/>
      </linearGradient>
    </defs>

    <rect class="faded-backdrop" x="0" y="400" width="848" height="800" fill="url(#faded-tones)"
          role="img" aria-label="Faded photo of the solar charging bench in a park"/>

    <path class="accent-band" d="M0,0 H848 V428 Q430,700 0,678 Z" fill="var(--brand-green)"/>
    <path class="hero-photo" d="M0,0 H848 V404 Q410,650 0,628 Z" fill="url(#hero-tones)"
          role="img" aria-label="Photo of the solar WiFi charging bench with white canopy, wooden seat and LED display, installed on grass outside a branch library"/>

    <circle class="logo-ring" cx="800" cy="-80" r="392" fill="var(--brand-blue)"/>
    <circle class="logo-disc" cx="816" cy="-92" r="384" fill="var(--paper)"/>

    <path class="footer-wave" d="M0,1112 Q380,1040 848,1080 V1200 H0 Z" fill="url(#footer-wave)"/>
  </svg>

  <div class="brand-name">
    <span class="brand-mark"></span>
    Marigold
    <span class="brand-sub">Renewables</span>
  </div>

  <ul class="feature-list">
    <li>LED Advertising display</li>
    <li>Connection to internet (User Defined)</li>
    <li>800W Solar</li>
    <li>USB-A and USB-C cell phone charging ports</li>
    <li>400ah battery backup with low voltage shutoff</li>
    <li>Insulated for -40 Deg C</li>
    <li>Wireless cell phone charging</li>
    <li>Vandalism resistant</li>
    <li>Theft resistant</li>
  </ul>

  <div class="social">
    <div class="social-icons">
      <span class="social-dot"></span>
      <span class="social-dot"></span>
      <span class="social-dot"></span>
    </div>
    @marigold renewables
  </div>
</main>
</body>
</html>
```